Wren's Home Care Business Card

Business card design
Font must be in Poppins Regular for Wren's Home Care
Kind Hands Every Day font is Alex Brush

Colour must be Hex #910E2B
RGB 145-14-43
Pantone 7427 C
We want the card editable
On the front please include
Name eg Marla Dunstow
Position eg Clinical Care Manager
Phone number mobile 0473 586 342
Phone 08 7394 2606
Email : marla@wrenshomecare-demo.com.au
Address : Quiet Cove, Western Australia, 6208
Website : wrenshomecare-demo.com.au
Contact us today to experience the warmth, respect and personal touch of Wren's Home Care.

Target Market(s)

35+

Industry/Entity Type

aged care / community

Contact Information for Business Card

see project description

Requirements
Must have
• Colours, logos and fonts as detailed and uploaded

```html
<!DOCTYPE html>
<html lang="en">
<head>
<meta charset="utf-8">
<title>Wren's Home Care – Business Card</title>
<link rel="stylesheet" href="https://fonts.googleapis.com/css2?family=Montserrat:wght@400;500;600;700&display=swap">
<style>
  :root {
    --brand: #910E2B;
    --brand-deep: #7C0B24;
    --brand-shade: #6E0A20;
    --ink: #1E1E1E;
    --paper: #FFFFFF;
    --backdrop: #E9E6E1;
  }
  * { box-sizing: border-box; margin: 0; padding: 0; }
  html, body { width: 900px; height: 1200px; overflow: hidden; }
  body { background: var(--backdrop); position: relative; font-family: "Montserrat", sans-serif; }

  .card { position: absolute; border-radius: 24px; overflow: hidden; }
  .card-front { left: 80px; top: 131px; width: 742px; height: 441px; background: var(--paper); }
  .card-back { left: 78px; top: 638px; width: 744px; height: 440px; background: var(--brand); }

  .brand-name {
    position: absolute; font-family: "Montserrat", sans-serif; font-weight: 500;
    color: var(--brand); line-height: 1.1; white-space: nowrap;
  }
  .card-front .brand-name { left: 38px; top: 72px; font-size: 34px; }
  .tagline {
    position: absolute; font-family: "Montserrat", sans-serif; font-weight: 400;
    color: var(--brand); white-space: nowrap;
  }
  .card-front .tagline { left: 39px; top: 124px; font-size: 18px; }

  .holder { position: absolute; right: 50px; top: 48px; text-align: right; }
  .holder-name { font-weight: 700; font-size: 27px; color: var(--brand); line-height: 1.1; }
  .holder-role { font-size: 16.5px; color: var(--ink); margin-top: 3px; }
  .edge-tab { position: absolute; right: 0; top: 48px; width: 25px; height: 53px; background: var(--brand); }

  .mark-spot {
    position: absolute; left: 430px; top: 134px; width: 296px; height: 296px;
    border-radius: 50%; background: var(--brand);
  }

  .address { position: absolute; left: 37px; top: 263px; font-size: 16.5px; color: var(--ink); line-height: 1.3; }
  .contacts { position: absolute; left: 40px; top: 324px; list-style: none; }
  .contacts li { display: flex; align-items: center; font-size: 16.5px; color: var(--ink); height: 23px; }
  .contacts svg { width: 15px; height: 15px; margin-right: 10px; fill: var(--brand); flex: none; }

  .back-spot {
    position: absolute; left: 102px; top: 127px; width: 168px; height: 168px;
    border-radius: 50%; background: var(--brand-deep);
  }
  .card-back .brand-name { left: 290px; top: 168px; font-size: 42px; color: var(--brand-shade); }
  .card-back .tagline { left: 292px; top: 226px; font-size: 21px; color: var(--brand-shade); }
  .closing {
    position: absolute; left: 0; right: 0; top: 356px; text-align: center;
    color: var(--paper); font-weight: 600; font-size: 16px; line-height: 1.4;
  }
</style>
</head>
<body>
  <section class="card card-front">
    <div class="brand-name">Wren's Home Care</div>
    <div class="tagline">Kind Hands Every Day</div>

    <div class="holder">
      <div class="holder-name">Marla Dunstow</div>
      <div class="holder-role">Managing Director</div>
    </div>
    <div class="edge-tab"></div>

    <div class="mark-spot" aria-hidden="true"></div>

    <p class="address">Quiet Cove,<br>Western Australia, 6208</p>
    <ul class="contacts">
      <li><svg viewBox="0 0 16 16"><path d="M2 5c0-2 2-3 6-3s6 1 6 3v1h-3V5H5v1H2z"/><path d="M4 7h8l2 7H2z"/><circle cx="8" cy="10.5" r="1.8" fill="#fff"/></svg>0473 586 342</li>
      <li><svg viewBox="0 0 16 16"><path d="M4 1l2.5 3-1.5 2c1 2 3 4 5 5l2-1.5 3 2.5-1.5 2.5C8 14 2 8 1.5 2.5z"/></svg>08 7394 2606</li>
      <li><svg viewBox="0 0 16 16"><path d="M1 3h14v1.5L8 9 1 4.5z"/><path d="M1 6.2l7 4.3 7-4.3V13H1z"/></svg>marla@wrenshomecare-demo.com.au</li>
      <li><svg viewBox="0 0 16 16"><circle cx="8" cy="8" r="7"/><path d="M4 5l3 1 1 3-2 1 1 3M10 2.5l1 3 3 1" stroke="#fff" stroke-width="1.3" fill="none"/></svg>wrenshomecare-demo.com.au</li>
    </ul>
  </section>

  <section class="card card-back">
    <div class="back-spot" aria-hidden="true"></div>
    <div class="brand-name">Wren's Home Care</div>
    <div class="tagline">Kind Hands Every Day</div>
    <p class="closing">Contact us today to experience the warmth,<br>respect and personal touch of Wren's Home Care.</p>
  </section>
</body>
</html>
```